Design a Professional Home Health Business Card

I am looking for a graphic designer who has the skill and creativity to redesign a business card to a more simple and modern beautiful design. I need a 3.5" x 2" design in Illustrator or Photoshop file format so it can easily be editable for us later on. I would like a front and back design.

The attachment are the old design for you to view and I uploaded the logo to use. Please create a second design mockup with showing the Voxlumen & Pelticora social icon as I would like to compare both design with icons and another without icons.

If you think you can handle this task, then I am waiting for your entrys to this project.

```html
<!DOCTYPE html>
<html lang="en">
<head>
<meta charset="utf-8">
<title>Lumora Home Health – Business Card</title>
<link rel="stylesheet" href="https://fonts.googleapis.com/css2?family=Montserrat:wght@400;500;600&display=swap">
<style>
  :root {
    --bg: #22384a;
    --sky: #5ba7de;
    --brand: #2f78bd;
    --white: #ffffff;
    --muted: #eaf4fc;
  }
  * { margin: 0; padding: 0; box-sizing: border-box; }
  html, body {
    width: 1200px; height: 900px; overflow: hidden;
    background: var(--bg);
    font-family: "Montserrat", sans-serif;
  }
  .stage { position: relative; width: 1200px; height: 900px; }
  .card {
    position: absolute; left: 386px; width: 430px; height: 246px;
    overflow: hidden; background: var(--sky);
  }
  .card-front { top: 191px; }
  .card-back { top: 466px; }
  .card svg.shape { position: absolute; inset: 0; }

  .brand {
    position: absolute; display: flex; align-items: center;
    color: var(--brand); font-weight: 500; white-space: nowrap; line-height: 1;
  }
  .brand-dot { flex: none; border-radius: 50%; background: var(--brand); }

  .card-front .brand {
    left: 0; right: 0; top: 108px; justify-content: center; gap: 12px; font-size: 29px;
  }
  .card-front .brand-dot { width: 24px; height: 24px; }

  .card-back .brand { left: 16px; top: 116px; gap: 7px; font-size: 15px; }
  .card-back .brand-dot { width: 12px; height: 12px; }

  .details { position: absolute; left: 232px; top: 32px; color: var(--white); }
  .person-name { font-size: 13.5px; font-weight: 600; }
  .person-role { font-size: 9.5px; color: var(--muted); margin-top: 2px; }
  .address { font-size: 9.5px; line-height: 1.45; color: var(--muted); margin-top: 12px; }
  .contact-list { list-style: none; margin-top: 8px; }
  .contact-list li {
    display: flex; align-items: center; gap: 9px;
    font-size: 8.8px; color: var(--muted); line-height: 16px;
  }
  .contact-list svg { width: 8px; height: 8px; flex: none; }
</style>
</head>
<body>
<main class="stage">

  <section class="card card-front" aria-label="Card front">
    <svg class="shape" viewBox="0 0 430 246" aria-hidden="true">
      <circle cx="215" cy="123" r="208" fill="none" stroke="#ffffff" stroke-width="2.5"/>
      <circle cx="215" cy="123" r="200" fill="#ffffff"/>
    </svg>
    <p class="brand"><span>Lumora Home Health</span><span class="brand-dot" aria-hidden="true"></span></p>
  </section>

  <section class="card card-back" aria-label="Card back">
    <svg class="shape" viewBox="0 0 430 246" aria-hidden="true">
      <circle cx="-267" cy="146" r="484" fill="none" stroke="#ffffff" stroke-width="2.5"/>
      <circle cx="-267" cy="146" r="476" fill="#ffffff"/>
    </svg>
    <p class="brand"><span>Lumora Home Health</span><span class="brand-dot" aria-hidden="true"></span></p>
    <div class="details">
      <p class="person-name">Talin Averian</p>
      <p class="person-role">President</p>
      <p class="address">Lumora Home Health, Inc.<br>418 W. Crestline Ave Unit 210<br>Fairmont, CA 90412</p>
      <ul class="contact-list">
        <li><svg viewBox="0 0 8 8"><rect x="2" y="0" width="4.5" height="8" rx="1" fill="#fff"/></svg>(555) 204-7316</li>
        <li><svg viewBox="0 0 8 8"><rect x="0.5" y="3" width="7" height="5" rx="1" fill="#fff"/><rect x="1.5" y="0.5" width="5" height="2" rx="1" fill="#fff"/></svg>(555) 381-2049</li>
        <li><svg viewBox="0 0 8 8"><rect x="0.5" y="2" width="7" height="5" rx="0.8" fill="#fff"/></svg>(555) 649-1825</li>
        <li><svg viewBox="0 0 8 8"><circle cx="4" cy="4" r="3.6" fill="#fff"/></svg>talin@lumorahomehealth.com</li>
        <li><svg viewBox="0 0 8 8"><circle cx="4" cy="4" r="3.3" fill="none" stroke="#fff" stroke-width="1.2"/></svg>www.lumorahomehealth.com</li>
      </ul>
    </div>
  </section>

</main>
</body>
</html>
```